Managed IT Service Provider Needs a Slick "Who We Are" or "Intro" Brochure

http://www.brellix.com/

tag line: Smart Network Solutions
Mission statement: Accelerating business through technology

We need a basic intro brochure that is snazzy, modern, and clean. It will not be a text heavy document. It needs to primarily introduce us, and discuss roughly our managed service offerings which we call "Steady Guard".

Once this intro doc is complete, we would like to work with the designer to complete some more product specific documents with the same look and feel. We are also interested in a matching business card design.

Here's a design we ran across and liked it: http://www.artbidhub.com/design/3849126

The design above has roughly the amount of text we'd like to see. It's clean, modern and fun. This is just an example of something we liked. Clean designs are great, not too busy.

It should talk about reliability, our professionalism, and our vigilance. We are stewards of information for our clients. This brochure doesn't need to provide a ton of information about our services, but should essentially be a call-to-action to contact us if you have a small to medium business and need a reliable technology partner to guide you.

Here's some older text:

Norvane is a leading edge Information Technology (IT) services company providing innovative solutions to all forms of IT challenges for small, medium and enterprise sized clients. Norvane has performed technology services in a multitude of industries including law enforcement, government, healthcare, educational, financial, broadcast and others. As a full service integrator, Norvane provides network design, installation, maintenance, and administration. Whether you are a client who uses our Managed Services offerings or our Consulting Services, you can expect Norvane’s certified professionals to achieve the best possible network performance, security and reliability using the most expeditious and cost effective methods available.

Some pics of our vans, an older capability doc (rough draft), and our logo in vector format is attached.

We are looking for something that flows with our website and vans.

We have a max of 5 days for this before we need to get them to the local printer for next Friday evening.

Target Market(s)

Small and Medium Business - Medical, Law, Engineering, Financial, other professional services firms.

Industry/Entity Type

Business

Contact Information for Business Card

Just looking for something that matches the doc design. Clean modern card. Should have our mission, maybe on the back: Accelerating business through technology

Font styles to use
Sans Serif

Requirements
Must have
• Modern tech design. Should flow with our website and van colors.
• I should add we are looking for a single 8.5" x 11" page, front and back, oriented vertically. We do not intend on folding this in any way. It will be inserted into a presentation folder with other materials.

```html
<!DOCTYPE html>
<html lang="en">
<head>
<meta charset="utf-8">
<title>Norvane – Who We Are</title>
<link href="https://fonts.googleapis.com/css2?family=Open+Sans:wght@400;600;700;800&display=swap" rel="stylesheet">
<style>
  :root {
    --brand-blue: #1f6fc4;
    --brand-blue-dark: #0f4c8f;
    --sky-mid: #9fb9d3;
    --steel: #5e7a96;
    --ink: #3c4650;
    --muted: #6b7782;
    --paper: #ffffff;
  }
  * { margin: 0; padding: 0; box-sizing: border-box; }
  html, body { width: 829px; height: 1200px; overflow: hidden; background: var(--paper); }
  body { font-family: "Open Sans", Arial, sans-serif; color: var(--ink); }

  .flyer { position: relative; width: 829px; height: 1200px; background: var(--paper); }

  .hero {
    position: absolute; left: 0; top: 0; width: 829px; height: 540px;
    background:
      radial-gradient(ellipse at 68% 50%, rgba(255,255,255,0.6), rgba(255,255,255,0) 55%),
      linear-gradient(180deg, #c9d9ea 0%, var(--sky-mid) 50%, var(--steel) 100%);
  }
  .hero-fade {
    position: absolute; left: 0; bottom: 0; width: 100%; height: 80px;
    background: linear-gradient(180deg, rgba(255,255,255,0) 0%, rgba(255,255,255,0.9) 100%);
  }

  .headline { position: absolute; right: 0; top: 40px; display: flex; flex-direction: column; align-items: flex-end; gap: 8px; }
  .headline-tag {
    background: var(--brand-blue); color: var(--paper);
    font-weight: 700; font-size: 30px; line-height: 1; padding: 12px 34px 12px 24px;
  }
  .headline-tag.secondary { background: var(--brand-blue-dark); font-size: 34px; }

  .content { position: absolute; left: 64px; right: 64px; top: 580px; }
  .section-title { color: var(--brand-blue); font-weight: 800; font-size: 40px; letter-spacing: 1px; margin-bottom: 24px; }

  .body-copy { font-size: 16px; line-height: 1.65; color: var(--ink); margin-bottom: 18px; }
  .body-copy strong { color: var(--brand-blue-dark); }

  .cta { margin-top: 24px; font-size: 17px; font-weight: 700; color: var(--brand-blue); }

  .brand { position: absolute; right: 64px; bottom: 60px; display: flex; align-items: center; gap: 12px; }
  .brand-dot { width: 30px; height: 30px; border-radius: 50%; background: var(--brand-blue); }
  .brand-name { font-weight: 700; font-size: 42px; color: var(--brand-blue-dark); line-height: 1; }
  .brand-tagline { font-size: 12px; color: var(--muted); letter-spacing: 1px; text-transform: uppercase; margin-top: 4px; }
</style>
</head>
<body>
  <main class="flyer">
    <section class="hero" role="img" aria-label="Photo of a businessman in a suit standing in a bright, blue-toned modern city office">
      <div class="hero-fade"></div>
      <div class="headline">
        <div class="headline-tag">When you have IT issues,</div>
        <div class="headline-tag secondary">We have IT solutions.</div>
      </div>
    </section>

    <section class="content">
      <h2 class="section-title">WHO WE ARE</h2>

      <p class="body-copy"><strong>Norvane</strong> is a leading edge Information Technology (IT) services company providing innovative solutions to all forms of IT challenges for small, medium and enterprise sized clients.</p>
      <p class="body-copy">Norvane has performed technology services in a multitude of industries including law enforcement, government, healthcare, educational, financial, broadcast and others. As a full service integrator, Norvane provides network design, installation, maintenance, and administration.</p>
      <p class="body-copy">Whether you are a client who uses our <strong>Steady Guard</strong> Managed Services offerings or our Consulting Services, you can expect Norvane’s certified professionals to achieve the best possible network performance, security and reliability.</p>

      <p class="cta">We provide FREE Personalized Assessment</p>
    </section>

    <div class="brand">
      <span class="brand-dot"></span>
      <div>
        <div class="brand-name">Norvane</div>
        <div class="brand-tagline">Smart Network Solutions</div>
      </div>
    </div>
  </main>
</body>
</html>
```